Two Versions of a Business Card for a Lawyer

Summary: I need a logo and a business card. The business card is two-sided and comes in two versions. One version is conservative, the other is slightly different with one or more pink embellishments in the logo or somewhere else in the business card.
I'm about to start off as a sole practitioner in criminal and immigration law. I'll largely be working with marginalised communities and in areas of social justice. One of my main focuses will be gendered violence, I'm hoping to specialise my practice towards representing victims of domestic and sexual violence and sex workers. I want a business card which would attract this clientele and make them feel safe to speak with me. I'd also like it to communicate a sense of hope.
However, the business card still has to be very conservative as the legal profession is very stuffy. So I was thinking of having two versions of the same card, one would be very straight forward while the other would have a **pink embellishment** or perhaps several. For example, if the scales of justice were used in the design, maybe the second version would have a pink flower about to bloom on the scale somewhere. Or maybe it's my logo that is different and pink.
While both designs have to be pretty conservative, I still want it to give off a sense that I'm alternative and think outside the box. With lawyers, I think a little bit of deviation goes a long way (less is more).
As far as colour goes (other than the pink embellishment), I was thinking something monochromatic, probably black and white but I am open to considering more colours. I personally love colour, and would love to use more colour, but am hesitant because of the nature of the profession. If you can find a way to use more colour while keeping it conservative and letting the pink pop, I'd be pretty pleased.
In general, I would prefer a clean simplistic design and logo. It should be immediately obvious that I'm a lawyer just by glancing at the card. I'm open to symbols of law, like the scales of justice or lady justice or something else. However, I don't want it to be the same as everyone else's.
Eventually, the design/style should be easy to recreate in the form of a website.
As far as the logo goes, it would probably use a circle as my last name starts with the letter "O". It can be very simple, with just my name and "Barrister & Solicitor". I don't currently have a logo, but the winning designer will be invited to provide a separate file for just the logo for an additional fee (I think it was CA$99). (Please ignore the uploaded logo file, it just wouldn't let me continue without uploading something).
As for the information that should go into the card, I'm still finalizing my address and phone number. So please use a placeholder for now.
Target Market(s)
Women, victims of sexual or domestic violence, refugees, people in need of legal services
Industry/Entity Type
Lawyer
Contact Information for Business Card
Maren Vickery
Barrister & Solicitor
LL.B., B.C.L., B.F.A.
Criminal & Immigration Law
Street address
Toronto, ON
Postal Code
Phone number
Fax number
Email
Logo Text
Maren Vickery, Barrister & Solicitor
Requirements
Must have
- Two versions
- One with pink
- Simplistic
Nice to have
- Maybe more colour
Should not have
- Not too conservative
- Not too predictable

```html
<!DOCTYPE html>
<html lang="en">
<head>
<meta charset="utf-8">
<title>Maren Vickery — Business Card</title>
<link rel="stylesheet" href="https://fonts.googleapis.com/css2?family=Crimson+Text:ital,wght@0,600;0,700;1,400;1,600;1,700&display=swap">
<style>
  :root {
    --rose: #cd6a8e;
    --rose-text: #d0678f;
    --paper: #ffffff;
    --ornament: #f1d6e0;
  }
  html, body {
    margin: 0;
    padding: 0;
    overflow: hidden;
    background: var(--paper);
  }
  .card {
    position: relative;
    width: 686px;
    height: 1200px;
    background: var(--paper);
    font-family: "Crimson Text", Georgia, serif;
    overflow: hidden;
  }
  .card__identity {
    position: absolute;
    left: 41px;
    top: 300px;
    color: var(--rose-text);
  }
  .card__name {
    margin: 0;
    font-style: italic;
    font-weight: 400;
    font-size: 80px;
    line-height: 1;
    letter-spacing: 0.5px;
  }
  .card__title {
    margin: 14px 0 0;
    font-weight: 700;
    font-size: 32px;
    line-height: 40px;
  }
  .card__practice {
    margin: 30px 0 0;
    font-style: italic;
    font-weight: 600;
    font-size: 38px;
    line-height: 1;
  }
  .card__band {
    position: absolute;
    left: 0;
    top: 606px;
    width: 686px;
    height: 594px;
    background: var(--rose);
  }
  .card__contact {
    list-style: none;
    margin: 0;
    padding: 0;
    position: absolute;
    left: 41px;
    top: 20px;
    color: var(--paper);
    font-style: italic;
    font-weight: 700;
    font-size: 32px;
    line-height: 57px;
  }
  .card__ornament {
    position: absolute;
    right: 22px;
    bottom: 12px;
    width: 168px;
    height: 166px;
  }
</style>
</head>
<body>
  <main class="card">
    <header class="card__identity">
      <h1 class="card__name">Maren Vickery</h1>
      <p class="card__title">Barrister &amp; Solicitor<br>LL.B., B.C.L., B.F.A.</p>
      <p class="card__practice">Criminal &amp; Immigration Law</p>
    </header>
    <section class="card__band">
      <ul class="card__contact">
        <li>Street address</li>
        <li>Toronto, ON</li>
        <li>Postal Code</li>
        <li>Phone number</li>
        <li>Fax number</li>
        <li>Email</li>
      </ul>
      <svg class="card__ornament" viewBox="0 0 168 166" role="img" aria-label="Decorative white flourish ornament">
        <rect x="0" y="0" width="168" height="166" rx="6" fill="var(--ornament)"/>
      </svg>
    </section>
  </main>
</body>
</html>
```